Single Webpage Custom Design

We need a single page for a service-offering on http://awareness.tovenquard.com/. I created a draft so you can see what content should be on that page.

```html
<!DOCTYPE html>
<html lang="en">
<head>
<meta charset="utf-8">
<title>Tovenquard – Security Awareness E-Learning</title>
<link href="https://fonts.googleapis.com/css2?family=Montserrat:wght@300;400;500;600;700;800&display=swap" rel="stylesheet">
<style>
:root{
  --ink:#1e3440;
  --muted:#5d6b74;
  --teal:#1fb3bd;
  --teal-dark:#128c96;
  --hero-bg:#e8fbfc;
  --soft:#f4f7f9;
  --footer:#07363a;
  --footer-bottom:#042b2f;
  --white:#ffffff;
  --line:#e3e9ec;
}
*{box-sizing:border-box;margin:0;padding:0}
html,body{width:1200px;height:2400px;overflow:hidden}
body{font-family:'Montserrat',sans-serif;color:var(--ink);background:var(--white);position:relative}
.abs{position:absolute}
.eyebrow{font-size:9px;font-weight:500;color:var(--teal);letter-spacing:.2px;text-transform:uppercase;line-height:1.4}
.h-strong{font-size:22px;font-weight:700;color:var(--ink);letter-spacing:.3px;line-height:1.15}
.h-light{font-size:22px;font-weight:300;color:#8a959c;letter-spacing:.3px;line-height:1.15}
.body-text{font-size:9.5px;line-height:1.6;color:var(--muted)}

/* header & hero */
.hero{left:0;top:0;width:1200px;height:336px;background:var(--hero-bg)}
.brand{left:175px;top:36px;display:flex;align-items:center;gap:8px;font-weight:800;font-size:22px;color:var(--ink)}
.brand-dot{width:22px;height:22px;border-radius:50%;background:#f5a623}
.nav-item{top:41px;font-size:10.5px;font-weight:500;color:var(--ink);white-space:nowrap}
.lang{left:935px;top:35px;width:86px;height:24px;border:1px solid #9aa6ad;border-radius:12px;display:flex;align-items:center;gap:5px;padding-left:8px;font-size:9px;background:var(--white)}
.hero-title{left:175px;top:148px;font-size:25px;font-weight:600;line-height:1.3;color:var(--ink);letter-spacing:.3px}
.hero-title .mark{background:linear-gradient(transparent 70%,#bfeef2 70%)}
.hero-sub{left:175px;top:228px;font-size:11.5px;line-height:1.7;color:var(--muted)}
.hero-figure{left:820px;top:90px;width:100px;height:246px;border-radius:40px 40px 0 0;background:linear-gradient(180deg,#f2e1d6 0%,#2b2b2f 55%,#1b1b1e 100%)}
.hero-deco{left:720px;top:60px;width:340px;height:276px}

/* design section */
.design{left:0;top:336px;width:1200px;height:489px;background:var(--white);overflow:hidden}
.design-rings{left:0;top:0;width:1200px;height:489px}
.design-copy{left:175px;top:60px;width:340px}
.design-copy .h-strong{margin-top:8px}
.design-copy .body-text{margin-top:12px}
.checklist{list-style:none;margin-top:4px}
.checklist li{font-size:9.5px;color:var(--muted);line-height:1.6;display:flex;align-items:center;gap:6px}
.checklist li::before{content:"";width:6px;height:6px;border-radius:50%;background:var(--ink)}
.explore{margin-top:12px;font-size:9.5px;font-weight:500;color:var(--teal)}
.video{left:566px;top:57px;width:454px;height:222px;background:linear-gradient(135deg,#2a0f5e 0%,#3d1a86 50%,#1b0a40 100%)}
.play{position:absolute;left:193px;top:77px;width:68px;height:68px;border-radius:50%;background:var(--teal);border:5px solid rgba(255,255,255,.35);display:flex;align-items:center;justify-content:center}
.video-bar{position:absolute;left:20px;right:160px;bottom:28px;height:3px;background:rgba(255,255,255,.35)}
.slide{top:321px;height:123px;color:var(--white);overflow:hidden}
.slide-cap{position:absolute;left:18px;bottom:10px;right:18px}
.slide-title{font-size:12px;font-weight:500;letter-spacing:.3px}
.slide-text{font-size:8.5px;line-height:1.3;margin-top:2px}
.slide-play{width:16px;height:16px;border-radius:50%;background:var(--white);display:flex;align-items:center;justify-content:center;margin-bottom:4px}
.slide-classic{left:206px;width:245px;background:linear-gradient(135deg,#0b2a4a,#1c5f8c 55%,#0a1f3a)}
.slide-avatar{left:473px;top:315px;width:266px;height:135px;background:linear-gradient(135deg,#2a0f5e,#44208e 60%,#1b0a40);box-shadow:0 8px 18px rgba(30,50,90,.3)}
.slide-onepager{left:761px;width:245px;background:linear-gradient(135deg,#e9e4df,#8c8478 50%,#2a2a2e)}
.arrow-nav{top:362px;width:24px;height:46px}

/* topics */
.topics{left:0;top:825px;width:1200px;height:498px;background:linear-gradient(180deg,#eef2f4 0%,#f7f9fa 50%,#eef2f4 100%)}
.topics-copy{left:176px;top:65px;width:850px}
.topics-copy .h-strong{margin-top:8px}
.topics-copy .body-text{margin-top:10px}
.card{top:207px;width:262px;background:var(--white);border-radius:4px;padding:22px 19px 18px;box-shadow:0 4px 18px rgba(40,70,90,.08)}
.card-icon{width:40px;height:40px;border-radius:50%;border:1.5px solid var(--teal);display:flex;align-items:center;justify-content:center}
.card-icon.filled{background:var(--teal)}
.card-title{margin-top:16px;font-size:11.5px;font-weight:500;color:var(--ink)}
.card-text{margin-top:7px;font-size:8px;line-height:1.35;color:var(--muted)}
.tags{margin-top:8px;display:grid;grid-template-columns:repeat(3,1fr);row-gap:5px}
.tags span{font-size:8px;color:#8a959c;display:flex;align-items:center;gap:4px}
.tags span::before{content:"";width:7px;height:7px;border-radius:50%;background:var(--ink)}
.card-arrow{display:flex;justify-content:flex-end;margin-top:10px}

/* customize */
.customize{left:0;top:1323px;width:1200px;height:444px;background:var(--soft)}
.stage{left:0;top:0;width:598px;height:444px;background:linear-gradient(180deg,#1e5fb0 0%,#1f5aa3 60%,#184c8f 100%)}
.pager{top:404px;height:32px;border-radius:16px;background:var(--white);display:flex;align-items:center;justify-content:space-between;padding:0 6px 0 16px;font-size:10px;color:var(--ink)}
.pager .circ{width:18px;height:18px;border-radius:50%;border:1px solid #b9c3c8;display:flex;align-items:center;justify-content:center}
.cust-copy{left:638px;top:56px;width:386px}
.cust-copy .h-strong{margin-top:8px}
.cust-copy .body-text{margin-top:12px}
.accordion{margin-top:12px;display:flex;flex-direction:column;gap:10px}
.acc-item{background:var(--white);border:1px solid var(--line);padding:0 16px;height:37px;display:flex;align-items:center;gap:10px;font-size:9.5px;font-weight:500;color:var(--ink)}
.acc-item.open{height:auto;flex-direction:column;align-items:flex-start;padding:12px 16px 16px;box-shadow:0 4px 14px rgba(40,70,90,.08)}
.acc-item.open .acc-head{display:flex;align-items:center;gap:10px;color:var(--teal)}
.acc-item.open p{font-size:9.5px;font-weight:400;line-height:1.7;color:var(--muted);margin-top:6px}

/* export */
.export-wrap{left:0;top:1767px;width:1200px;height:354px;background:var(--white);overflow:hidden}
.export{left:175px;top:60px;width:850px;height:238px;border-radius:24px;background:linear-gradient(120deg,#3ab4bd 0%,#2ba3ad 45%,#138592 100%);color:var(--white);text-align:center;overflow:hidden}
.export-kicker{margin-top:54px;font-size:11px;font-weight:500;letter-spacing:.3px}
.export-title{margin-top:8px;font-size:32px;font-weight:800;line-height:1.1}
.export-sub{font-size:32px;font-weight:300;line-height:1.1}
.scorm-btn{margin:12px auto 0;width:192px;height:46px;border-radius:23px;background:var(--white);color:var(--teal);display:flex;align-items:center;justify-content:center;gap:8px;font-size:17px;font-weight:500}

/* footer */
.footer{left:0;top:2121px;width:1200px;height:224px;background:var(--footer);color:var(--white)}
.f-col{top:68px}
.f-head{font-size:10px;font-weight:600;letter-spacing:.2px}
.f-row{display:flex;gap:8px;align-items:flex-start;margin-top:10px;font-size:7.5px;line-height:1.45}
.f-pin{width:18px;height:18px;border-radius:50%;background:var(--teal);flex:none;display:flex;align-items:center;justify-content:center}
.f-links{list-style:none;margin-top:14px}
.f-links li{font-size:8px;line-height:1.95}
.socials{display:flex;gap:9px;margin-top:14px}
.socials span{width:25px;height:25px;border-radius:50%;background:#2a5357}
.search{margin-top:16px;width:176px;height:32px;border-radius:16px;background:var(--white);display:flex;align-items:center;justify-content:space-between;padding:0 4px 0 16px;font-size:8px;color:#8a959c}
.search-btn{width:26px;height:26px;border-radius:50%;background:var(--teal);display:flex;align-items:center;justify-content:center}
.f-lang{margin-top:12px;width:176px;height:32px;border-radius:16px;background:var(--white);display:flex;align-items:center;gap:8px;padding:0 12px;font-size:8.5px;color:var(--muted)}
.f-bottom{left:0;top:2345px;width:1200px;height:55px;background:var(--footer-bottom);color:var(--white);font-size:8px;display:flex;align-items:center;justify-content:space-between;padding:0 175px}
</style>
</head>
<body>

<!-- header & hero -->
<section class="abs hero">
  <div class="abs brand"><span class="brand-dot"></span>Tovenquard</div>
  <nav>
    <span class="abs nav-item" style="left:482px">HOME</span>
    <span class="abs nav-item" style="left:557px">SOLUTION</span>
    <span class="abs nav-item" style="left:655px">PRICING</span>
    <span class="abs nav-item" style="left:744px">RESOURCES</span>
    <span class="abs nav-item" style="left:855px">ABOUT US</span>
  </nav>
  <div class="abs lang">
    <svg width="11" height="11" viewBox="0 0 12 12"><circle cx="6" cy="6" r="5" fill="none" stroke="#5d6b74"/><ellipse cx="6" cy="6" rx="2.2" ry="5" fill="none" stroke="#5d6b74"/><line x1="1" y1="6" x2="11" y2="6" stroke="#5d6b74"/></svg>
    English
    <svg width="7" height="5" viewBox="0 0 7 5" style="margin-left:8px"><path d="M1 1l2.5 2.5L6 1" fill="none" stroke="#5d6b74"/></svg>
  </div>
  <h1 class="abs hero-title">SECURITY AWARENESS E-LEARNING<br><span class="mark">YOU CAN RUN</span> IN YOUR <span class="mark">ENVIROMENT</span></h1>
  <p class="abs hero-sub">Choose one or multiple training modules from Tovenquard Security and<br>import them into your learning management system (LMS) via SCORM</p>
  <svg class="abs hero-deco" viewBox="0 0 340 276">
    <circle cx="47" cy="50" r="6" fill="none" stroke="#7fd8df" stroke-width="2.5"/>
    <polygon points="18,112 28,104 29,118" fill="#9be3c6"/>
    <rect x="267" y="82" width="12" height="12" transform="rotate(45 273 88)" fill="none" stroke="#7fd8df" stroke-width="2"/>
    <circle cx="247" cy="147" r="17" fill="#7fd8df"/>
    <circle cx="46" cy="207" r="17" fill="#c5f0f3"/>
    <circle cx="197" cy="252" r="6" fill="#7fd8df"/>
    <rect x="72" y="30" width="30" height="246" fill="#ffffff"/>
  </svg>
  <div class="abs hero-figure" role="img" aria-label="Photo of a smiling businesswoman peeking out and pointing toward the headline"></div>
</section>

<!-- design -->
<section class="abs design">
  <svg class="abs design-rings" viewBox="0 0 1200 489">
    <circle cx="375" cy="250" r="222" fill="none" stroke="#e6ecef"/>
    <circle cx="190" cy="300" r="200" fill="none" stroke="#eef2f4"/>
  </svg>
  <div class="abs design-copy">
    <p class="eyebrow">Design is more then just layout -<br>it is about the desired user experience</p>
    <h2 class="h-strong">CHOOSE YOUR</h2>
    <p class="h-light">PREFERED DESIGN</p>
    <p class="body-text">Lorem Ipsum is simply dummy text of the printing &amp; typesetting industry. Lorem Ipsum has been the industry's standard dummy text ever since</p>
    <ul class="checklist">
      <li>Do you want to include video in course?</li>
      <li>Should the text be read to the user?</li>
      <li>Do you want to include a game or exam at the end of the course?</li>
      <li>Do you want to guide the user with an avatar through the course?</li>
    </ul>
    <p class="explore">EXPLOR A FEW DESIGN TYPES &rarr;</p>
  </div>
  <div class="abs video" role="img" aria-label="Video still of a purple security illustration titled Avatar Design Security Incidents">
    <div class="play"><svg width="20" height="22" viewBox="0 0 20 22"><polygon points="2,1 19,11 2,21" fill="#fff"/></svg></div>
    <div class="video-bar"></div>
  </div>
  <svg class="abs arrow-nav" style="left:126px" viewBox="0 0 24 46"><path d="M20 2L3 23l17 21" fill="none" stroke="#9aa6ad" stroke-width="1.5"/></svg>
  <div class="abs slide slide-classic" role="img" aria-label="Thumbnail of a glowing padlock over a presenting audience">
    <div class="slide-cap"><div class="slide-play"><svg width="6" height="7" viewBox="0 0 6 7"><polygon points="0,0 6,3.5 0,7" fill="#128c96"/></svg></div><p class="slide-title">CLASSIC DESIGN</p><p class="slide-text">Lorem Ipsum is simply dummy text of the printing and typesetting industry.</p></div>
  </div>
  <div class="abs slide slide-avatar" role="img" aria-label="Thumbnail of the purple avatar design security illustration">
    <div class="slide-cap"><div class="slide-play"><svg width="6" height="7" viewBox="0 0 6 7"><polygon points="0,0 6,3.5 0,7" fill="#128c96"/></svg></div><p class="slide-title">AVATAR DESIGN</p><p class="slide-text">Lorem Ipsum is simply dummy text of the printing and typesetting industry.</p></div>
  </div>
  <div class="abs slide slide-onepager" role="img" aria-label="Thumbnail photo of a person working at a computer screen with code">
    <div class="slide-cap"><div class="slide-play"><svg width="6" height="7" viewBox="0 0 6 7"><polygon points="0,0 6,3.5 0,7" fill="#128c96"/></svg></div><p class="slide-title">ONE PAGER</p><p class="slide-text">Lorem Ipsum is simply dummy text of the printing and typesetting industry.</p></div>
  </div>
  <svg class="abs arrow-nav" style="left:1052px" viewBox="0 0 24 46"><path d="M4 2l17 21L4 44" fill="none" stroke="#9aa6ad" stroke-width="1.5"/></svg>
</section>

<!-- topics -->
<section class="abs topics" role="img" aria-label="Faint blurred office photo behind the topics section">
  <div class="abs topics-copy">
    <p class="eyebrow">Select the topics and the specify the course lenght</p>
    <h2 class="h-strong">CHOOSE YOUR</h2>
    <p class="h-light">TOPICS</p>
    <p class="body-text">Lorem Ipsum is simply dummy text of the printing and typesetting industry. Lorem Ipsum has been the industry's standard dummy text ever since the 1500s, when an unknown printer took a galley of type and scrambled it to make a type specimen book. It has survived not only five centuries, but also the leap into electronic typesetting, remaining essentially unchanged. It was popularised in the 1960s with the release of Letraset sheets containing Lorem Ipsum passages.</p>
  </div>
  <article class="abs card" style="left:175px">
    <div class="card-icon filled"><svg width="18" height="16" viewBox="0 0 18 16"><rect x="1" y="2" width="16" height="11" rx="1" fill="none" stroke="#fff" stroke-width="1.4"/><line x1="4" y1="6" x2="14" y2="6" stroke="#fff"/><line x1="4" y1="9" x2="11" y2="9" stroke="#fff"/></svg></div>
    <h3 class="card-title">STANDARD TRAINING</h3>
    <p class="card-text">Lorem Ipsum is simply dummy text of the printing and typesetting industry. Lorem Ipsum has been the industry standard dummy text ever since the1500s, when an unknown printer took a galley of type and scrambled it to make a type specimen book</p>
    <div class="tags"><span>TVQ Security</span><span>TVQ Security</span><span>TVQ Security</span><span>TVQ Security</span><span>TVQ Security</span><span>TVQ Security</span><span>TVQ Security</span><span>TVQ Security</span><span>TVQ Security</span><span>TVQ Security</span><span>TVQ Security</span><span>TVQ Security</span><span>TVQ Security</span><span>TVQ Security</span><span>TVQ Security</span></div>
    <div class="card-arrow"><svg width="16" height="10" viewBox="0 0 16 10"><path d="M15 5H2M6 1L2 5l4 4" fill="none" stroke="#1fb3bd" stroke-width="1.4"/></svg></div>
  </article>
  <article class="abs card" style="left:468px">
    <div class="card-icon"><svg width="18" height="16" viewBox="0 0 18 16"><rect x="1" y="3" width="16" height="10" rx="1" fill="none" stroke="#1fb3bd" stroke-width="1.3"/><rect x="4" y="6" width="5" height="4" fill="none" stroke="#1fb3bd"/><line x1="11" y1="7" x2="14" y2="7" stroke="#1fb3bd"/></svg></div>
    <h3 class="card-title">CUSTOMIZED TRAINING</h3>
    <p class="card-text">Lorem Ipsum is simply dummy text of the printing and typesetting industry. Lorem Ipsum has been the industry's standard dummy text ever since...</p>
    <div class="tags"><span>TVQ Security</span><span>TVQ Security</span><span>TVQ Security</span><span>TVQ Security</span><span>TVQ Security</span><span>TVQ Security</span><span>TVQ Security</span><span>TVQ Security</span><span>TVQ Security</span><span>TVQ Security</span><span>TVQ Security</span><span>TVQ Security</span></div>
    <div class="card-arrow"><svg width="16" height="10" viewBox="0 0 16 10"><path d="M1 5h13M10 1l4 4-4 4" fill="none" stroke="#1e3440" stroke-width="1.4"/></svg></div>
  </article>
  <article class="abs card" style="left:758px">
    <div class="card-icon"><svg width="18" height="16" viewBox="0 0 18 16"><rect x="1" y="4" width="12" height="9" rx="1" fill="none" stroke="#1fb3bd" stroke-width="1.3"/><circle cx="14" cy="4" r="2.5" fill="none" stroke="#1fb3bd"/><path d="M11 12c0-2 1.5-3.5 3-3.5s3 1.5 3 3.5" fill="none" stroke="#1fb3bd"/></svg></div>
    <h3 class="card-title">INDIVIDUAL TRAINING</h3>
    <p class="card-text">Lorem Ipsum is simply dummy text of the printing and typesetting industry. Lorem Ipsum has been the industry's standard dummy text ever since...</p>
    <div class="tags"><span>TVQ Security</span><span>TVQ Security</span><span>TVQ Security</span><span>TVQ Security</span><span>TVQ Security</span><span>TVQ Security</span><span>TVQ Security</span><span>TVQ Security</span><span>TVQ Security</span><span>TVQ Security</span><span>TVQ Security</span><span>TVQ Security</span></div>
    <div class="card-arrow"><svg width="16" height="10" viewBox="0 0 16 10"><path d="M1 5h13M10 1l4 4-4 4" fill="none" stroke="#1e3440" stroke-width="1.4"/></svg></div>
  </article>
</section>

<!-- customize -->
<section class="abs customize">
  <div class="abs stage" role="img" aria-label="Illustration of a presenter pointing at a chart on a projection screen in front of a seated audience"></div>
  <div class="abs pager" style="left:175px;width:104px">Previous<span class="circ"><svg width="8" height="6" viewBox="0 0 8 6"><path d="M7 3H1M3 1L1 3l2 2" fill="none" stroke="#1fb3bd"/></svg></span></div>
  <div class="abs pager" style="left:313px;width:104px">Next<span class="circ"><svg width="8" height="6" viewBox="0 0 8 6"><path d="M1 3h6M5 1l2 2-2 2" fill="none" stroke="#9aa6ad"/></svg></span></div>
  <div class="abs cust-copy">
    <p class="eyebrow">You might ask yourself why it needs customization?</p>
    <h2 class="h-strong">CUSTOMIZE!</h2>
    <p class="h-light">BESIDE JUST ADJUSTING THE</p>
    <p class="body-text">Lorem Ipsum is simply dummy text of the printing &amp; typesetting industry. Lorem Ipsum has been the industry's standard dummy text ever since</p>
    <div class="accordion">
      <div class="acc-item"><svg width="14" height="14" viewBox="0 0 14 14"><rect x="1" y="3" width="7" height="10" fill="none" stroke="#1fb3bd"/><rect x="8" y="6" width="5" height="7" fill="none" stroke="#1fb3bd"/></svg>FROM CEO:</div>
      <div class="acc-item"><svg width="14" height="14" viewBox="0 0 14 14"><rect x="2" y="1" width="10" height="12" fill="none" stroke="#1fb3bd"/><line x1="4" y1="5" x2="10" y2="5" stroke="#1fb3bd"/><line x1="4" y1="8" x2="10" y2="8" stroke="#1fb3bd"/></svg>DO YOU KNOW OUR POLICIES?</div>
      <div class="acc-item open">
        <div class="acc-head"><svg width="14" height="14" viewBox="0 0 14 14"><path d="M1 4h9v6H5l-3 2v-2H1z" fill="none" stroke="#1fb3bd"/><path d="M5 2h8v6" fill="none" stroke="#1fb3bd"/></svg>GET THE MESSAGE RIGHT !</div>
        <p>Lorem ipsum dolor sit amet, consectetur adipisicing elit, sed do eiusmod tempor incididunt labore et dolore magna aliqua. Ut enim ad minim veniam, quis nostrud exercitation ullamco laboris niesi ut aliquip ex ea commodo .</p>
      </div>
    </div>
  </div>
</section>

<!-- export -->
<section class="abs export-wrap">
  <svg class="abs" style="left:0;top:0" width="1200" height="354" viewBox="0 0 1200 354">
    <circle cx="370" cy="190" r="170" fill="none" stroke="#eef2f4"/>
    <circle cx="1090" cy="60" r="60" fill="none" stroke="#e6ecef"/>
    <circle cx="1130" cy="90" r="80" fill="none" stroke="#eef2f4"/>
  </svg>
  <div class="abs export" role="img" aria-label="Teal tinted photo of people working at a desk behind the export banner">
    <p class="export-kicker">LOREM IPSUM IS SIMPLY DUMMY TEXT OF THE PRINTING &amp; TYPESETTING.</p>
    <h2 class="export-title">EXPORT (SCORM)</h2>
    <p class="export-sub">LOREM IPSUM IS SIMPLY DUMMY</p>
    <div class="scorm-btn"><svg width="26" height="24" viewBox="0 0 26 24"><rect x="2" y="5" width="18" height="17" rx="2" fill="none" stroke="#1fb3bd" stroke-width="1.5"/><rect x="6" y="2" width="18" height="17" rx="2" fill="#fff" stroke="#1fb3bd" stroke-width="1.5"/><circle cx="15" cy="10.5" r="4" fill="none" stroke="#1fb3bd" stroke-width="1.5"/></svg>SCORM</div>
  </div>
</section>

<!-- footer -->
<footer class="abs footer">
  <div class="abs f-col" style="left:175px;width:220px">
    <p class="f-head">CONTACT US</p>
    <div class="f-row" style="margin-top:14px"><span class="f-pin"><svg width="8" height="10" viewBox="0 0 8 10"><path d="M4 9C1.5 6 1 4.8 1 4a3 3 0 016 0c0 .8-.5 2-3 5z" fill="none" stroke="#fff"/></svg></span><span>Europe : Tovenquard Security AG Lindenweg 12<br>| 6301 Baar | Switzerland</span></div>
    <div class="f-row"><span class="f-pin"><svg width="8" height="10" viewBox="0 0 8 10"><path d="M4 9C1.5 6 1 4.8 1 4a3 3 0 016 0c0 .8-.5 2-3 5z" fill="none" stroke="#fff"/></svg></span><span>North America : Tovenquard Security<br>USA 4820 Meridian Ave Suite 210<br>Denver, CO 80203</span></div>
    <div class="f-row"><span class="f-pin"><svg width="9" height="9" viewBox="0 0 9 9"><path d="M2 1l1.5 2-1 1c.5 1 1.5 2 2.5 2.5l1-1L8 7l-1 1.5C4 8 1 5 .5 2z" fill="none" stroke="#fff"/></svg></span><span style="padding-top:4px">Phone Global: +41 44 000 12 34</span></div>
  </div>
  <div class="abs f-col" style="left:523px">
    <p class="f-head">QUICK LINKS</p>
    <ul class="f-links"><li>Home</li><li>Solution</li><li>Pricing</li><li>Resources</li><li>About Us</li><li>Support Wiki</li></ul>
  </div>
  <div class="abs f-col" style="left:705px">
    <p class="f-head">CONNECT</p>
    <div class="socials"><span></span><span></span><span></span></div>
  </div>
  <div class="abs f-col" style="left:850px">
    <p class="f-head">SEARCH</p>
    <div class="search">Search<span class="search-btn"><svg width="12" height="12" viewBox="0 0 12 12"><circle cx="5" cy="5" r="3.8" fill="none" stroke="#fff" stroke-width="1.3"/><line x1="8" y1="8" x2="11" y2="11" stroke="#fff" stroke-width="1.3"/></svg></span></div>
    <div class="f-lang"><svg width="14" height="14" viewBox="0 0 12 12"><circle cx="6" cy="6" r="5" fill="none" stroke="#5d6b74"/><ellipse cx="6" cy="6" rx="2.2" ry="5" fill="none" stroke="#5d6b74"/><line x1="1" y1="6" x2="11" y2="6" stroke="#5d6b74"/></svg>English Language<svg width="7" height="5" viewBox="0 0 7 5" style="margin-left:auto"><path d="M1 1l2.5 2.5L6 1" fill="none" stroke="#5d6b74"/></svg></div>
  </div>
</footer>
<div class="abs f-bottom"><span>All rights reserved © 2020 Lorem Ipsum Services.</span><span>Terms of use &nbsp;&nbsp; | &nbsp;&nbsp; Privacy policy</span></div>

</body>
</html>
```